Invitation Design for TORAM KELPANE Investigator Event (Exclusive Cocktail Reception)

Project Overview:
Toram Cellworks is hosting an exclusive, invitation-only cocktail reception for KELPANE clinical study investigators during the ODRIM 2026 Conference. We need a polished, high-end event invitation designed for both email and print formats.
Event Details:
Event Name: Gather & Grow: The KELPANE Investigator Event
Date: Saturday, January 24
Time: 5:00–7:00 PM
Location: Walter Brisk Chophouse (Hartwell Private Room), Orlean Terrace
Purpose: A relaxed, come-and-go cocktail reception for KELPANE investigators to mingle; light content and conversation, no formal presentations.
Design Requirements:
Two logos required:
TORAM (primary)
KELPANE (secondary)
Color Palette: Use the Toram color scheme, KELPANE color scheme, or a clean blend of both.
Tone & Style: Premium, modern, medical-professional with a high-end reception feel
Deliverable Layout:
Event title
Date & time
Location
Blurb: You are invited to a gathering for KELPANE clinical investigators. This event is intended to provide an opportunity for professional discussion, study related updates, and peer connection within the investigator community.
Both required logos
Clean, elegant spacing with strong hierarchy
What We Want
A visually striking but clean design that feels:
Sophisticated and corporate-professional
Consistent with our brand aesthetic
Appropriate for a high-profile physician audience
Think: elevated, clinical, modern — not flashy or overly busy.
Audience
Physicians and researchers participating in the KELPANE clinical study — a high-end, professional group.

```html
<!DOCTYPE html>
<html lang="en">
<head>
<meta charset="utf-8">
<title>Gather &amp; Grow: The KELPANE Investigator Event</title>
<link rel="stylesheet" href="https://fonts.googleapis.com/css2?family=Source+Serif+4:wght@600;700&family=Roboto:wght@400;500;700&display=swap">
<style>
  :root{
    --page:#bcbdbf;
    --paper:#f3f2ec;
    --orange:#e5882a;
    --navy:#1b2a5a;
    --ink:#4a4a4a;
    --green:#8cc63f;
    --rule-green:#9ccc5a;
    --blue-soft:#8fa6d8;
  }
  *{box-sizing:border-box;margin:0;padding:0}
  html,body{width:1200px;height:1200px;overflow:hidden;background:var(--page)}
  .canvas{position:relative;width:1200px;height:1200px;background:var(--page)}
  .invite{
    position:absolute;left:0;top:304px;width:1200px;height:575px;
    background:var(--paper);overflow:hidden;
    font-family:"Roboto",Arial,sans-serif;color:var(--navy);text-align:center;
  }
  .corner-art{position:absolute;width:240px;height:190px}
  .corner-art.tl{left:0;top:0;background:radial-gradient(circle at 0 0,rgba(143,166,216,.28),rgba(229,136,42,.12) 55%,transparent 75%)}
  .corner-art.tr{right:0;top:0;background:radial-gradient(circle at 100% 0,rgba(143,166,216,.28),rgba(229,136,42,.12) 55%,transparent 75%)}
  .corner-art.bl{left:0;bottom:0;background:radial-gradient(circle at 0 100%,rgba(156,204,90,.26),rgba(229,136,42,.14) 55%,transparent 75%)}
  .corner-art.br{right:0;bottom:0;background:radial-gradient(circle at 100% 100%,rgba(156,204,90,.26),rgba(229,136,42,.14) 55%,transparent 75%)}
  .event-title{
    position:absolute;left:0;right:0;top:30px;
    font-family:"Source Serif 4",Georgia,serif;font-weight:700;
    font-size:62px;line-height:1;color:var(--orange);
  }
  .rule{position:absolute;left:50%;height:2px;transform:translateX(-50%)}
  .rule.orange{top:114px;width:400px;background:linear-gradient(90deg,transparent,var(--orange),transparent)}
  .rule.navy{top:200px;width:320px;background:linear-gradient(90deg,transparent,var(--navy),transparent)}
  .rule.green{top:352px;width:320px;background:linear-gradient(90deg,transparent,var(--rule-green),transparent)}
  .event-subtitle{
    position:absolute;left:0;right:0;top:138px;
    font-family:"Source Serif 4",Georgia,serif;font-weight:700;
    font-size:40px;line-height:1;color:var(--navy);
  }
  .details{position:absolute;left:0;right:0;top:218px;font-size:24px;line-height:29px}
  .details .date{font-weight:700;font-size:25px}
  .details strong{font-weight:700}
  .blurb{
    position:absolute;left:50%;top:370px;width:470px;transform:translateX(-50%);
    font-size:18.5px;line-height:21.5px;color:var(--ink);
  }
  .brands{
    position:absolute;left:0;right:0;top:480px;height:60px;
    display:flex;justify-content:center;align-items:center;
  }
  .brand-primary{
    width:180px;text-align:right;padding-right:40px;
    font-family:"Roboto",Arial,sans-serif;font-weight:500;font-size:40px;color:var(--green);
  }
  .brand-divider{width:1px;height:60px;background:var(--navy)}
  .brand-secondary{width:220px;text-align:left;padding-left:34px;color:var(--navy)}
  .brand-secondary .name{display:flex;align-items:center;gap:8px;font-weight:700;font-size:30px;line-height:1}
  .brand-secondary .mark{width:14px;height:14px;border-radius:50%;background:var(--navy)}
  .brand-secondary .tagline{font-size:6px;font-weight:500;margin-top:4px;padding-left:22px;white-space:nowrap}
</style>
</head>
<body>
<div class="canvas">
  <section class="invite">
    <div class="corner-art tl" role="img" aria-label="Decorative arcs in blue, green and orange"></div>
    <div class="corner-art tr" role="img" aria-label="Decorative arcs in blue, green and orange"></div>
    <div class="corner-art bl" role="img" aria-label="Decorative arcs in green and orange"></div>
    <div class="corner-art br" role="img" aria-label="Decorative arcs in green and orange"></div>

    <h1 class="event-title">Gather &amp; Grow</h1>
    <div class="rule orange"></div>
    <h2 class="event-subtitle">The KELPANE Investigator Event</h2>
    <div class="rule navy"></div>

    <div class="details">
      <p class="date">Saturday, January 24</p>
      <p>5:00 – 7:00 PM</p>
      <p><strong>Walter Brisk Chophouse</strong> (Hartwell Private Room)</p>
      <p>Orlean Terrace</p>
    </div>
    <div class="rule green"></div>

    <p class="blurb">You are invited to a gathering for KELPANE clinical investigators. This event intendede to opportunity for a professional discussion, study related updates, and peer connection within investigator community.</p>

    <div class="brands">
      <div class="brand-primary">TORAM</div>
      <div class="brand-divider"></div>
      <div class="brand-secondary">
        <div class="name"><span class="mark"></span>KELPANE U.S.</div>
        <div class="tagline">A Multicenter Randomized Controlled Cell Study Trial Program</div>
      </div>
    </div>
  </section>
</div>
</body>
</html>
```